Web Design Project - Old Brackley (Bar)

We need a website for a new wine bar/hotel opening in Sydney's Kings Cross area. The concept is a rustic Australiana bar. We intend to use raw materials (sandstone, rusty metal etc) and lots of greenery/plants. It is set to be stylish and accessible to a young and middle age clientele.

The idea is to bring the outside inside.

The venue can cater for 450 people and is in one of the major nightclub strips in Australia. The demographic differs from celebrities to backpackers.

Target Market(s)

We are targeting 23yr - 40yr olds.

Industry/Entity Type

Hotel

Requirements
Must have
• What I want is a design to reflect is the fit out of the bar. We would like to see a rustic design to reflect the theme of the bar. The theme behind the fit out will be "bringing the outside inside" with lots of plants, wet walls etc.. There will be exposed brickwork, sandstone, timber and rusted steel with laser cut designs throughout the venue.
Nice to have
• I've attached some 3D designs that the venue will be roughly based on.

```html
<!DOCTYPE html>
<html lang="en">
<head>
<meta charset="utf-8">
<title>Old Brackley</title>
<link rel="stylesheet" href="https://fonts.googleapis.com/css2?family=Cabin:wght@400;500;700&family=Philosopher&family=Cinzel:wght@400;700&display=swap">
<style>
:root{
  --brick:#9a5040;
  --brick-light:#b8705e;
  --mortar:#b9aaa0;
  --leaf:#7f9a32;
  --leaf-dark:#4f6a1c;
  --leaf-gold:#c99a34;
  --red:#b3060b;
  --red-dark:#7d0206;
  --red-text:#8a0c0c;
  --leather:#5a2416;
  --wood:#b8622a;
  --wood-light:#cf7a3a;
  --wood-dark:#8c3f17;
  --panel:#ffffff;
  --text:#6a6a6a;
  --title:#3a3a3a;
  --cream:#f3e6c8;
  --footer:#4a1d12;
  --rule:#cfcfcf;
}
*{box-sizing:border-box;margin:0;padding:0}
html,body{width:851px;height:1200px;overflow:hidden}
body{position:relative;background:var(--leather);font-family:Arial,Helvetica,sans-serif;color:var(--text)}
.abs{position:absolute}

.brick-top{left:0;top:0;width:851px;height:92px;
  background:
    radial-gradient(ellipse 220px 70px at 425px 40px,rgba(200,190,180,.35),transparent 70%),
    linear-gradient(90deg,var(--brick-light),var(--brick) 25%,#a65c4a 50%,var(--brick) 75%,var(--brick-light)),
    var(--brick)}
.brick-top::after{content:"";position:absolute;inset:0;background:linear-gradient(180deg,rgba(185,170,160,.25),transparent 40%,rgba(60,20,10,.35))}
.leaves-left{left:70px;top:0;width:125px;height:140px;background:radial-gradient(ellipse 60px 65px at 60px 70px,var(--leaf),var(--leaf-dark) 70%,transparent 72%)}
.leaves-right{left:400px;top:0;width:160px;height:125px;background:radial-gradient(ellipse 35px 30px at 35px 30px,var(--leaf),transparent 72%),radial-gradient(ellipse 55px 55px at 105px 60px,var(--leaf-gold),#8a7a22 65%,transparent 72%)}
.brick-bottom{left:0;top:1160px;width:851px;height:40px;background:linear-gradient(180deg,#8d4d3e,#a8685a 60%,#b59e95)}
.logo{left:215px;top:0;width:150px;height:88px;background:radial-gradient(ellipse 80px 50px at 75px 40px,#ece4c6,#d9cca4 70%,rgba(200,185,150,.7));text-align:center}
.logo-mark{display:inline-block;width:26px;height:26px;margin-top:22px;background:#1b1b1b}
.logo-name{font-family:Cinzel,serif;font-size:15px;color:#1b1b1b;letter-spacing:1px;margin-top:8px}

.nav-band{left:0;top:88px;width:851px;height:38px;background:linear-gradient(180deg,#c4151a,var(--red-dark))}
.nav{left:145px;top:85px;width:561px;height:38px;background:linear-gradient(180deg,#d21a1f,var(--red) 55%,#930207);display:flex;align-items:center;font-family:Cabin,sans-serif;font-weight:500;font-size:12px;color:#fff}
.nav a{color:#fff;text-decoration:none;height:38px;line-height:38px;text-align:center;border-right:1px solid rgba(0,0,0,.2)}
.nav a.home{width:153px;text-align:left;padding-left:83px}
.nav a.blog{width:68px}
.nav a.menu{width:89px}
.nav a.feat{width:86px}
.nav a.res{width:95px;border:none}
.nav a.active{background:#fff;color:var(--red)}
.nav .star{margin-left:auto;margin-right:14px;color:#f7c62a;font-size:11px}
.caret{font-size:8px;margin-left:5px}

.dropdown{left:298px;top:122px;width:143px;background:#fff;box-shadow:0 2px 6px rgba(0,0,0,.4);font-family:Cabin,sans-serif;font-size:9px;font-weight:500;color:var(--red-text);z-index:3}
.dropdown div{height:25px;line-height:25px;padding:0 16px;border-bottom:1px solid #e4e4e4}
.dropdown div.hl{background:#ececec}
.dropdown .arr{float:right}

.slider{left:145px;top:122px;width:561px;height:206px;background:linear-gradient(100deg,#6b2a2e,#c65a62 40%,#9b3a44 60%,#3a1216)}
.side-tab{top:190px;width:12px;height:105px;background:linear-gradient(180deg,#b56130,#8a3e1c);font-family:Cabin,sans-serif;font-size:7px;color:#3a1508;writing-mode:vertical-rl;text-align:center;line-height:12px}
.caption{left:160px;top:262px;width:385px;height:51px;background:rgba(30,15,15,.82);border:1px solid rgba(255,255,255,.2);padding:5px 11px;color:#fff}
.caption h2{font-family:Cabin,sans-serif;font-size:11.5px;font-weight:500;margin-bottom:6px}
.caption p{font-size:7.5px;line-height:11px;color:#ddd}
.dots{left:373px;top:320px;width:105px;height:14px;background:#7a3a20;border-radius:7px;display:flex;justify-content:center;align-items:center;gap:6px}
.dots i{width:6px;height:6px;border-radius:50%;background:#d48a46}
.dots i.on{background:#3a1508}

.wood{left:0;top:330px;width:851px;height:670px;
  background:
    linear-gradient(180deg,rgba(60,20,5,.35),transparent 6%,transparent 94%,rgba(60,20,5,.35)),
    linear-gradient(90deg,#a24d1f,var(--wood) 12%,#c36c30 24%,var(--wood-light) 38%,#c26a2e 50%,var(--wood) 62%,#c97434 76%,var(--wood) 88%,#a24d1f)}

.feature{top:348px;width:150px;color:#fff}
.feature .icon{width:28px;height:28px;border-radius:50%;background:#f1dfb8;float:left;margin-right:12px}
.feature h3{font-family:Philosopher,sans-serif;font-weight:400;font-size:14px;line-height:28px;color:var(--cream)}
.feature p{clear:both;font-size:7.5px;font-weight:700;line-height:11px;margin-top:9px;color:#fff;height:33px}
.btn-more{display:inline-block;height:13px;line-height:13px;padding:0 14px 0 5px;font-size:6.5px;font-weight:700;color:#fff;background:linear-gradient(180deg,#d21a1f,#9a0308);clip-path:polygon(0 0,88% 0,100% 50%,88% 100%,0 100%)}
.feature .btn-more{margin-top:9px}

.panel{background:var(--panel);border-radius:3px;box-shadow:0 0 6px rgba(0,0,0,.35)}
.panel-main{left:145px;top:460px;width:392px;height:520px}
.panel-events{left:553px;top:460px;width:153px;height:520px}
.ribbon{height:28px;line-height:28px;background:linear-gradient(180deg,#c8141a,#8c0207);color:#fff;font-family:Cabin,sans-serif;font-weight:700;font-size:12px;padding-left:19px;clip-path:polygon(0 0,100% 0,92% 50%,100% 100%,0 100%)}
.show-link{font-size:6px;color:#777;text-decoration:underline}

.intro{left:160px;top:512px;width:363px;font-size:7px;line-height:10.5px;color:var(--text)}
.intro .drop{float:left;font-family:Cinzel,serif;font-weight:700;font-size:22px;line-height:20px;color:#5a2a20;margin-right:4px}
.divider{height:1px;background:var(--rule);position:absolute}
.divider::after{content:"~";position:absolute;left:50%;top:-8px;transform:translateX(-50%);background:#fff;padding:0 4px;font-size:11px;color:#999}

.dish{width:107px}
.dish h4{font-size:7.5px;font-weight:700;color:var(--title);margin-bottom:6px}
.dish .photo{position:relative;height:72px;background:linear-gradient(135deg,#d9c6a6,#b45a3a 55%,#6e8f3a)}
.dish .price{position:absolute;right:0;top:2px;background:#e01a12;color:#fff;font-size:10px;font-weight:700;padding:1px 4px}
.dish p{font-size:6.5px;line-height:9.5px;margin:8px 0 6px;height:30px}

.wide-btn{height:19px;line-height:19px;text-align:center;border:1px solid #ccc;border-radius:3px;background:linear-gradient(180deg,#fff,#e6e6e6);font-size:8.5px;color:#333}
.to-top{font-size:5.5px;color:#999;text-align:center}

.event{left:567px;width:125px}
.event .date{font-size:6.5px;font-weight:700;color:var(--red-text);padding-left:12px;position:relative}
.event .date::before{content:"";position:absolute;left:0;top:0;width:7px;height:7px;border:1.5px solid var(--red-text);border-radius:50%}
.event h4{font-size:7.5px;font-weight:700;color:#333;margin:6px 0;line-height:11px}
.event p{font-size:6.5px;line-height:10.5px;margin-bottom:6px;height:42px}

.footer{left:0;top:1000px;width:851px;height:160px;background:linear-gradient(180deg,#3e1309,var(--footer) 40%,#3a1208);border-top:1px solid #6a3020}
.foot-title{font-family:Philosopher,sans-serif;font-size:12px;color:var(--cream);font-weight:700}
.foot-row{font-size:7px;color:#d9c3ae;display:flex;align-items:center;gap:7px}
.foot-row .sq{width:12px;height:12px;background:#6a8fbf;flex:none}
.map{left:557px;top:1051px;width:149px;height:80px;background:linear-gradient(135deg,#c8d6e8,#e9e4d6 50%,#cfd9c4)}
</style>
</head>
<body>

<div class="abs brick-top" role="img" aria-label="Exposed red brick wall"></div>
<div class="abs logo">
  <span class="logo-mark"></span>
  <div class="logo-name">OLD BRACKLEY</div>
</div>

<div class="abs nav-band"></div>
<div class="abs leaves-left" role="img" aria-label="Green vine leaves hanging over the wall"></div>
<div class="abs leaves-right" role="img" aria-label="Golden vine leaves hanging over the wall"></div>
<div class="abs slider" role="img" aria-label="Guest holding a glass of red wine"></div>
<div class="abs side-tab" style="left:132px">PREVIOUS</div>
<div class="abs side-tab" style="left:707px">NEXT</div>

<nav class="abs nav">
  <a class="home">Homepage</a>
  <a class="blog active">Blog<span class="caret">&#9660;</span></a>
  <a class="menu">Menu Card</a>
  <a class="feat">Features<span class="caret">&#9660;</span></a>
  <a class="res">Reservations</a>
  <span class="star">&#9733;</span>
</nav>

<div class="abs dropdown">
  <div>Single post test blog entry</div>
  <div>Complete blog list</div>
  <div class="hl">Full width page</div>
  <div>Second level menu <span class="arr">&rsaquo;</span></div>
</div>

<div class="abs caption">
  <h2>Quisque lorem urna, mollis hendrerit lacinia vitae, suscipit non ante</h2>
  <p>Share a glass in our leafy courtyard of ferns, timber and old brick<br>walls, open late every night of the week for friends.</p>
</div>
<div class="abs dots"><i></i><i class="on"></i><i></i><i></i></div>

<div class="abs wood" role="img" aria-label="Warm timber plank background"></div>

<div class="abs feature" style="left:145px">
  <div class="icon" role="img" aria-label="Pizza"></div>
  <h3>Fantastic Pizzas</h3>
  <p>Thin crust baked daily in our brick oven with fresh local toppings and herbs.</p>
  <span class="btn-more">Read more</span>
</div>
<div class="abs feature" style="left:355px">
  <div class="icon" role="img" aria-label="Coffee cup"></div>
  <h3>Amazing Coffee</h3>
  <p>Single origin beans roasted nearby, poured by baristas who care about each cup.</p>
  <span class="btn-more">Read more</span>
</div>
<div class="abs feature" style="left:565px">
  <div class="icon" role="img" aria-label="Salad bowl"></div>
  <h3>Great Salads</h3>
  <p>Crisp garden greens, fresh herbs and house dressings served all day long.</p>
  <span class="btn-more">Read more</span>
</div>

<div class="abs panel panel-main"></div>
<div class="abs ribbon" style="left:140px;top:470px;width:208px">Most popular menu offerings</div>
<span class="abs show-link" style="left:472px;top:480px">show menu card</span>

<div class="abs intro"><span class="drop">S</span>Our kitchen cooks honest food from nearby farms, paired with a wine list built around small Australian makers. Every plate is made to share, whether you drop in after work or settle in for a long night. Ask staff about the seasonal specials and our cellar picks for the week.</div>

<div class="divider" style="left:160px;top:567px;width:363px"></div>

<div class="abs dish" style="left:160px;top:580px">
  <h4>Italian pasta</h4>
  <div class="photo" role="img" aria-label="Pasta dish"><span class="price">$4,99</span></div>
  <p>Hand rolled pasta with slow cooked ragu, parmesan and fresh basil.</p>
  <span class="btn-more">Read more</span>
</div>
<div class="abs dish" style="left:288px;top:580px">
  <h4>Baked meat</h4>
  <div class="photo" role="img" aria-label="Baked meat with juice"><span class="price">$8,00</span></div>
  <p>Oven roasted lamb shoulder with rosemary, garlic and crisp potatoes.</p>
  <span class="btn-more">Read more</span>
</div>
<div class="abs dish" style="left:416px;top:580px">
  <h4>Split pea soup</h4>
  <div class="photo" role="img" aria-label="Split pea soup"><span class="price">$2,99</span></div>
  <p>Thick green pea soup with smoked ham and warm crusty bread.</p>
  <span class="btn-more">Read more</span>
</div>

<div class="divider" style="left:160px;top:740px;width:363px"></div>

<div class="abs dish" style="left:160px;top:754px">
  <h4>Caesar salad</h4>
  <div class="photo" role="img" aria-label="Caesar salad"><span class="price">$1,99</span></div>
  <p>Cos lettuce, shaved parmesan, croutons and a tangy anchovy dressing.</p>
  <span class="btn-more">Read more</span>
</div>
<div class="abs dish" style="left:288px;top:754px">
  <h4>Chinese chicken</h4>
  <div class="photo" role="img" aria-label="Spring rolls with chicken"><span class="price">$2,99</span></div>
  <p>Crispy rolls of spiced chicken with chilli sauce and fresh greens.</p>
  <span class="btn-more">Read more</span>
</div>
<div class="abs dish" style="left:416px;top:754px">
  <h4>American apple pie</h4>
  <div class="photo" role="img" aria-label="Apple pie plate"><span class="price">$5,99</span></div>
  <p>Warm spiced apples in buttery pastry with a scoop of vanilla cream.</p>
  <span class="btn-more">Read more</span>
</div>

<div class="divider" style="left:160px;top:915px;width:363px"></div>
<div class="abs wide-btn" style="left:160px;top:933px;width:363px">Show entire menu card</div>
<div class="abs to-top" style="left:145px;top:964px;width:392px">&#8593; go back to the top</div>

<div class="abs panel panel-events"></div>
<div class="abs ribbon" style="left:548px;top:470px;width:88px">Events</div>
<span class="abs show-link" style="left:666px;top:480px">show all</span>

<div class="abs event" style="top:513px">
  <div class="date">11 / 05 / 2013 &nbsp;&bull;&nbsp; 9:30 PM</div>
  <h4>Vestibulum eu orci libero</h4>
  <p>Live acoustic sets in the fern garden with share plates and a glass of local wine.</p>
  <span class="btn-more">Read more</span>
</div>
<div class="divider" style="left:567px;top:618px;width:125px"></div>
<div class="abs event" style="top:633px">
  <div class="date">11 / 01 / 2013 &nbsp;&bull;&nbsp; 7:00 PM</div>
  <h4>Cras risus turpis, egestas necongue an ornare</h4>
  <p>A winemaker dinner of five courses paired with cellar releases.</p>
  <span class="btn-more">Read more</span>
</div>
<div class="divider" style="left:567px;top:737px;width:125px"></div>
<div class="abs event" style="top:752px">
  <div class="date">10 / 26 / 2013 &nbsp;&bull;&nbsp; 12:00 AM</div>
  <h4>Maecenas tincidunt quam</h4>
  <p>Midnight party with guest DJs out on the terrace until the early hours.</p>
  <span class="btn-more">Read more</span>
</div>
<div class="divider" style="left:567px;top:856px;width:125px"></div>
<div class="abs wide-btn" style="left:567px;top:873px;width:125px">Show all events</div>
<div class="abs to-top" style="left:553px;top:964px;width:153px">&#8593; go back to the top</div>

<div class="abs footer"></div>

<div class="abs foot-title" style="left:146px;top:1026px">Contact Information</div>
<svg class="abs" style="left:146px;top:1052px" width="12" height="14" viewBox="0 0 12 14"><path d="M6 0a5 5 0 0 1 5 5c0 4-5 9-5 9S1 9 1 5a5 5 0 0 1 5-5z" fill="#d2261c"/><circle cx="6" cy="5" r="2" fill="#fff"/></svg>
<div class="abs" style="left:170px;top:1052px;font-size:8px;font-weight:700;color:#e8d6c2">&ldquo;Old Brackley&rdquo;</div>
<div class="abs" style="left:170px;top:1066px;font-size:6.5px;color:#d9c3ae">48 Marlow Lane, Sydney, NSW, 2011</div>
<svg class="abs" style="left:144px;top:1099px" width="15" height="12" viewBox="0 0 15 12"><path d="M1 4c0-3 13-3 13 0v2h-3V4H4v2H1z M3 6h9l2 6H1z" fill="#bdbdbd"/></svg>
<div class="abs" style="left:168px;top:1098px;font-size:13px;color:#eee">+1 (555) 210 7788</div>
<svg class="abs" style="left:144px;top:1119px" width="14" height="10" viewBox="0 0 14 10"><rect width="14" height="10" fill="#e8b34a"/><path d="M0 0l7 6 7-6" fill="none" stroke="#9a6a14"/></svg>
<div class="abs" style="left:168px;top:1120px;font-size:7px;font-weight:700;color:#e8d6c2;text-decoration:underline">bookings@oldbrackley.com</div>

<div class="abs foot-title" style="left:370px;top:1026px">Social Networks</div>
<div class="abs foot-row" style="left:370px;top:1053px"><span class="sq"></span>Follow us on Chirper</div>
<div class="abs foot-row" style="left:370px;top:1070px"><span class="sq"></span>Become our friend on Friendbook</div>
<div class="abs foot-row" style="left:370px;top:1089px"><span class="sq"></span>Check us out on ProNet</div>
<div class="abs foot-row" style="left:370px;top:1120px"><span class="sq" style="background:#e8772a"></span>Check out our RSS feeds</div>

<div class="abs foot-title" style="left:555px;top:1026px">Where To Find Us</div>
<div class="abs map" role="img" aria-label="Street map showing the venue location"></div>

<div class="abs brick-bottom" role="img" aria-label="Exposed brick wall"></div>

</body>
</html>
```